BrightpathHR Brochure

We need a Brochure design for a Human Resources company based in Windhoek Namibia. We do general HR admin, payroll, disciplinary hearings, recruitment. We would like a design which can be used to print hardcopies as well as pdf versions.

Industry/Entity Type

Human Resource

Colors

Designer to choose colors to be used in the design.

Requirements
Nice to have
• relevant pictures

```html
<!DOCTYPE html>
<html lang="en">
<head>
<meta charset="utf-8">
<title>BrightpathHR Brochure</title>
<link href="https://fonts.googleapis.com/css2?family=Oswald:wght@500;600;700&family=Roboto+Condensed:wght@400;700&family=Source+Sans+3:wght@300;400;600;700&display=swap" rel="stylesheet">
<style>
:root{
  --backdrop:#c49a6c;
  --blue:#1677c4;
  --blue-deep:#1b5fa8;
  --navy:#1c4f8f;
  --yellow:#f2b529;
  --yellow-deep:#e9a51b;
  --green:#8cc63f;
  --green-deep:#4f8a1e;
  --teal:#5fc3c0;
  --ink:#1d1d1d;
  --grey:#555;
  --white:#fff;
}
*{margin:0;padding:0;box-sizing:border-box}
html,body{width:1200px;height:831px;overflow:hidden}
body{background:var(--backdrop);font-family:"Source Sans 3",sans-serif;position:relative;color:var(--ink)}
.side-label{position:absolute;top:30px;color:var(--white);font:700 25px "Source Sans 3",sans-serif;letter-spacing:.5px}
.side-label--back{left:213px}
.side-label--front{left:830px;top:33px}
.page{position:absolute;background:var(--white);overflow:hidden;box-shadow:4px 6px 10px rgba(0,0,0,.35)}
.page--back{left:40px;top:77px;width:547px;height:707px}
.page--front{left:614px;top:75px;width:548px;height:709px}
.abs{position:absolute}
.photo{position:absolute}

/* back page */
.approach-title{left:24px;top:22px;font:700 26px "Oswald",sans-serif;color:var(--blue-deep);letter-spacing:.3px}
.approach-intro{left:24px;top:66px;width:320px;font:700 8px/11.5px "Source Sans 3",sans-serif}
.col-heading{font:700 13.5px "Source Sans 3",sans-serif;color:var(--blue-deep)}
.col-text{font:400 8px/11px "Source Sans 3",sans-serif;color:var(--ink)}
.col-divider{left:204px;top:118px;width:1px;height:122px;background:#d5d5d5}
.brand{display:flex;align-items:center;gap:6px;font:600 19px "Source Sans 3",sans-serif;color:var(--blue-deep)}
.brand-dot{width:18px;height:18px;border-radius:50%;background:var(--navy)}
.what-we-do{left:352px;top:146px;width:166px;height:152px;background:var(--yellow);border-radius:8px 8px 0 0}
.what-we-do h3{position:absolute;left:22px;top:30px;font:600 19px "Source Sans 3",sans-serif;color:var(--navy)}
.wwd-list{position:absolute;left:14px;top:62px;list-style:none}
.wwd-list li{display:flex;gap:6px;margin-bottom:9px}
.wwd-list svg{flex:none;margin-top:2px}
.wwd-list b{display:block;font:700 10px "Source Sans 3",sans-serif;color:var(--white)}
.wwd-list span{display:block;font:400 7px "Source Sans 3",sans-serif;color:#fff6dc}
.back-band{left:0;top:432px;width:547px;height:275px;background:var(--blue)}
.contact-lead{left:20px;top:588px;width:204px;text-align:center;color:#dbe9f7;font:300 11px/16px "Source Sans 3",sans-serif}
.contact-email{left:0;top:630px;width:245px;text-align:center;color:var(--white);font:600 14px "Source Sans 3",sans-serif;letter-spacing:.3px}
.contact-phone{left:0;top:658px;width:245px;text-align:center;color:var(--white);font:700 25px "Roboto Condensed",sans-serif}
.services-title{left:265px;top:475px;color:var(--white);font:600 21px "Source Sans 3",sans-serif}
.services-list{left:265px;top:509px;width:280px;list-style:none;color:var(--white);font:400 11px/14px "Source Sans 3",sans-serif}
.services-list li{position:relative;padding-left:18px;margin-bottom:4.6px}
.services-list li::before{content:"";position:absolute;left:0;top:3px;width:8px;height:8px;border-radius:50%;background:radial-gradient(circle at 35% 35%,#d8ef8a,var(--green-deep))}
.follow{left:242px;top:663px;display:flex;align-items:center;gap:6px}
.follow-label{font:700 italic 15px "Source Sans 3",sans-serif;color:var(--yellow);margin-right:10px}
.social-square{width:19px;height:19px;background:#dbe9f7;border-radius:2px}

/* front page */
.consult-badge{left:44px;top:261px;width:146px;height:146px;border-radius:50%;background:radial-gradient(circle at 45% 35%,#a6d04a,#5e8f1e 70%,#3d6612);border:4px solid #d8e98c;box-shadow:0 0 0 3px var(--navy);display:flex;align-items:center;justify-content:center;text-align:center;color:var(--white);font:600 22px/25px "Source Sans 3",sans-serif}
.portrait-ring{left:353px;top:234px;width:172px;height:172px;border-radius:50%;background:var(--yellow);padding:8px}
.portrait-ring .photo{position:static;width:100%;height:100%;border-radius:50%;background:linear-gradient(160deg,#e9eef3,#b8c6d4 60%,#6d7f93)}
.front-brand{left:0;top:452px;width:548px;justify-content:center;font-size:30px}
.front-brand .brand-dot{width:24px;height:24px}
.headline{left:0;top:485px;width:548px;text-align:center;font:700 30px/34px "Oswald",sans-serif;color:var(--blue-deep);letter-spacing:.2px}
.promise-strip{left:46px;top:556px;width:458px;height:23px;background:var(--yellow-deep);border-radius:4px;display:flex;align-items:center;justify-content:center;gap:8px;font:700 11.5px "Roboto Condensed",sans-serif;color:var(--white)}
.promise-strip i{width:1px;height:15px;background:#fff4d0}
.front-intro{left:52px;top:586px;width:446px;text-align:center;font:400 7.6px/10.8px "Source Sans 3",sans-serif;color:var(--ink)}
.front-band{left:0;top:628px;width:548px;height:81px;background:var(--blue)}
.address-tag{left:134px;top:628px;width:270px;height:25px;background:var(--yellow);clip-path:polygon(0 0,100% 0,96% 100%,4% 100%);display:flex;align-items:center;justify-content:center;font:700 11px "Source Sans 3",sans-serif;color:var(--ink)}
.front-rule{left:30px;top:663px;width:490px;height:1px;background:#7fb4e2}
.front-contact{left:30px;top:668px;width:490px;display:flex;align-items:center;color:var(--white);font:700 16px "Roboto Condensed",sans-serif}
.front-contact .dot{width:13px;height:13px;border-radius:50%;background:var(--yellow-deep);margin:0 10px 0 14px}
.front-contact .call{font-size:20px}
</style>
</head>
<body>

<div class="side-label side-label--back">BACK</div>
<div class="side-label side-label--front">FRONT</div>

<!-- BACK PAGE -->
<section class="page page--back">
  <svg class="abs" style="left:0;top:0" width="547" height="70" viewBox="0 0 547 70">
    <path d="M250 0 C330 10 420 40 547 36 L547 0Z" fill="#dbe9f7"/>
    <path d="M290 0 C380 22 460 50 547 50 L547 42 C460 42 390 20 330 0Z" fill="#cfe27a"/>
    <path d="M330 0 C400 30 470 52 547 52 L547 38 C470 38 410 18 370 0Z" fill="#f2b529"/>
    <path d="M360 0 C420 22 480 40 547 40 L547 0Z" fill="var(--blue)"/>
  </svg>

  <h1 class="abs approach-title">OUR APPROACH</h1>
  <p class="abs approach-intro">Each company is unique. One-size-fits-all approaches will never help your business reach its full potential. We deliver custom solutions, tailored to you – your industry, your culture, your one-of-a-kind challenges.</p>

  <div class="photo" role="img" aria-label="Photo of two colleagues planning with sticky notes on a glass wall in a bright office" style="left:0;top:250px;width:350px;height:182px;background:linear-gradient(90deg,#c9a07a 0%,#e8cdb0 35%,#f7eee4 70%,#fff 100%)"></div>

  <h2 class="abs col-heading" style="left:26px;top:111px">Vision</h2>
  <p class="abs col-text" style="left:26px;top:135px;width:176px">To be a leading provider of HR consultancy and outsourcing services in Namibia.</p>
  <h2 class="abs col-heading" style="left:26px;top:165px">Mission</h2>
  <p class="abs col-text" style="left:26px;top:191px;width:176px">The mission of Brightpath Human Resources is dedicated to the highest quality of Customer Service, delivered with a sense of warmth and friendliness.</p>
  <div class="abs col-divider"></div>
  <h2 class="abs col-heading" style="left:221px;top:111px">Our Clients</h2>
  <p class="abs col-text" style="left:221px;top:137px;width:122px;color:var(--grey)">Whether you are a one-person business looking for an all-in-one assistance with all your human resources functions, or a corporate company wishing to outsource its human resources functions, Brightpath HR is here for you.</p>

  <div class="abs brand" style="left:370px;top:108px"><span class="brand-dot"></span>BrightpathHR</div>

  <div class="abs what-we-do">
    <svg class="abs" style="left:12px;top:0" width="142" height="18" viewBox="0 0 142 18"><path d="M0 0 H142 L132 14 Q130 18 124 18 H18 Q12 18 10 14Z" fill="var(--teal)"/></svg>
    <h3>What We Do</h3>
    <ul class="wwd-list">
      <li><svg width="10" height="10" viewBox="0 0 10 10"><circle cx="5" cy="5" r="5" fill="var(--navy)"/><path d="M2.6 5.2 4.3 6.8 7.5 3.4" stroke="#fff" stroke-width="1.4" fill="none"/></svg><div><b>EXPERT ANALYSIS</b><span>Identifying your NEEDS</span></div></li>
      <li><svg width="10" height="10" viewBox="0 0 10 10"><circle cx="5" cy="5" r="5" fill="var(--navy)"/><path d="M2.6 5.2 4.3 6.8 7.5 3.4" stroke="#fff" stroke-width="1.4" fill="none"/></svg><div><b>STRATEGIC PLANNING</b><span>Crafting a plan to take you there</span></div></li>
      <li><svg width="10" height="10" viewBox="0 0 10 10"><circle cx="5" cy="5" r="5" fill="var(--navy)"/><path d="M2.6 5.2 4.3 6.8 7.5 3.4" stroke="#fff" stroke-width="1.4" fill="none"/></svg><div><b>RISK MANAGEMENT</b><span>Minimizing your risks along the way</span></div></li>
    </ul>
  </div>
  <div class="photo" role="img" aria-label="Photo of a hand placing a blue HR jigsaw piece among puzzle pieces labelled with HR topics" style="left:352px;top:298px;width:166px;height:117px;border-radius:0 0 8px 8px;background:linear-gradient(135deg,#f1f1f3,#d6d8de 55%,#b5a79a)"></div>

  <div class="abs back-band"></div>
  <div class="photo" role="img" aria-label="Photo of a payroll binder on a weekly time sheet with a pen and calculator" style="left:26px;top:449px;width:188px;height:125px;background:linear-gradient(160deg,#e6c36a 0%,#7fb2dc 35%,#eef2f6 65%,#b9bec5)"></div>
  <p class="abs contact-lead">Interested in seeing what we can do for you? Please feel free to contact us:</p>
  <p class="abs contact-email">hello@brightpathhr.com</p>
  <p class="abs contact-phone">+264 81 555 0142</p>

  <h2 class="abs services-title">Services offered</h2>
  <ul class="abs services-list">
    <li>Payroll - administration of your monthly payroll;</li>
    <li>Recruitment - screening, selection and appointment;</li>
    <li>Compiling employment contracts;</li>
    <li>Assisting with disciplinary hearing processes;</li>
    <li>General HR admin functions, i.e. Social Security, Medical aid, Pension; and</li>
    <li>Affirmative Action reports.</li>
  </ul>

  <div class="abs follow">
    <span class="follow-label">Follow Us</span>
    <span class="social-square"></span><span class="social-square"></span><span class="social-square"></span>
  </div>
</section>

<!-- FRONT PAGE -->
<section class="page page--front" style="background:linear-gradient(180deg,#fff 55%,#d9e9f7 85%)">
  <div class="photo" role="img" aria-label="Photo of a hand arranging green HR letters on a grey surface with the words Human and Resource" style="left:0;top:0;width:548px;height:360px;background:linear-gradient(150deg,#8e8a84 0%,#c9c3ba 45%,#ddd6cc 80%);clip-path:path('M0 0 H548 V250 C470 330 330 360 180 355 C100 352 40 340 0 320 Z')"></div>
  <svg class="abs" style="left:0;top:0" width="548" height="380" viewBox="0 0 548 380">
    <path d="M528 0 C548 120 520 260 420 320 C320 370 150 370 0 330 L0 345 C160 385 330 385 430 335 C540 275 556 130 548 0Z" fill="var(--blue)"/>
    <path d="M516 0 C536 110 510 240 420 300 L428 306 C524 246 546 120 526 0Z" fill="var(--yellow)"/>
    <path d="M504 0 C520 90 500 200 430 270 L436 276 C510 206 532 100 514 0Z" fill="var(--green)"/>
    <path d="M492 0 C506 70 492 160 440 230 L446 234 C500 166 516 80 502 0Z" fill="#dbe9f7"/>
  </svg>

  <div class="abs consult-badge">HR<br>Consulting<br>Services</div>
  <div class="abs portrait-ring">
    <div class="photo" role="img" aria-label="Photo of a smiling professional woman with glasses at her desk in an office"></div>
  </div>

  <div class="abs brand front-brand"><span class="brand-dot"></span>BrightpathHR</div>

  <h1 class="abs headline">GENERAL HR ADMIN, PAYROLL,<br>DISCIPLINARY HEARINGS, RECRUITMENT</h1>

  <div class="abs promise-strip"><span>STRATEGIES that work.</span><i></i><span>ADVICE you can rely on.</span><i></i><span>EXPERTS who've been there.</span></div>

  <p class="abs front-intro">We offer a range of HR consulting services, all designed to help your company reach its potential. Whether you're looking for a small tweak or complete overhaul, we have you covered. Our services are available a la carte so you can get precisely what you need.</p>

  <div class="abs front-band"></div>
  <div class="abs address-tag">P O Box 40210 Acacia Square Windhoek Namibia.</div>
  <div class="abs front-rule"></div>
  <div class="abs front-contact">
    <span>http://www.brightpathhr.com</span><span class="dot"></span><span class="call">Call Us: +264 81 555 0142</span>
  </div>
</section>

</body>
</html>
```